Produktbroschüre
Zielgruppe
Einzelhändler im Einrichtungs-, Geschenk- und Blumanfachhandel, Dekorateure, Innenarchitekten,
Aufgabenstellung
Ich bin Existenzgründer und brauche eine ansprechende Produktbroschüre für Inneneinrichtungsdeko und Accessoires.
Die Artikel wechseln öfter und ich möchte in der Lage sein Bilder und Texte einfach auszutauschen. Über die zeit, wird das Sortiment erwetert, die Broschüre sollte einfach mitwachsen können.
Momentan behelfe ich mir mit Scribus und Gimp für Windows, bin aber kein Experte.
Als Anhang meine momentane, selbst gebaute Broschüre.

```html
<!DOCTYPE html>
<html lang="de">
<head>
<meta charset="utf-8">
<title>sorel bunt – Produktbroschüre</title>
<link href="https://fonts.googleapis.com/css2?family=Open+Sans:ital,wght@0,400;0,600;0,700;1,400;1,600;1,700&display=swap" rel="stylesheet">
<style>
:root{
  --orange:#f18a00;
  --orange-dark:#d97800;
  --ink:#333;
  --muted:#8a8a8a;
  --ghost:#f0f0f0;
  --paper:#fff;
  --stage:#e6e4e1;
}
*{box-sizing:border-box;margin:0;padding:0}
html,body{width:1200px;height:848px;overflow:hidden}
body{background:var(--stage);font-family:"Open Sans",Arial,sans-serif;color:var(--ink);position:relative}
.spread{position:absolute;width:496px;height:256px;display:flex;box-shadow:0 2px 6px rgba(0,0,0,.18)}
.page{position:relative;width:248px;height:256px;background:var(--paper);overflow:hidden}
.page.left{border-right:1px solid #ececec}
.ghost{position:absolute;top:14px;left:14px;font-size:28px;font-weight:700;font-style:italic;color:var(--ghost);letter-spacing:.5px;white-space:nowrap}
.page.right .ghost{left:auto;right:10px}
.running{position:absolute;top:14px;font-size:7px;font-weight:700;font-style:italic;color:#555;white-space:nowrap}
.page.left .running{left:44px}
.page.right .running{left:26px}
.frame{position:absolute;top:52px;height:140px;border:1.5px solid var(--orange);border-radius:7px;background:var(--paper)}
.page.left .frame{left:10px;width:228px}
.page.right .frame{left:12px;width:216px}
.photo{position:absolute;inset:8px 14px;border-radius:3px}
.tab{position:absolute;top:92px;width:20px;height:72px;background:var(--orange);color:#fff;font-size:8px;font-weight:600;writing-mode:vertical-rl;display:flex;align-items:center;justify-content:center;border-radius:3px}
.page.right .tab{right:6px}
.page.left .tab{left:2px;transform:rotate(180deg)}
.tab.long{height:96px;top:80px}
.caption{position:absolute;top:184px;width:96px;height:40px;background:var(--orange);color:#fff;text-align:center;padding-top:8px;border-radius:3px}
.caption strong{display:block;font-size:8.5px;font-weight:700}
.caption span{display:block;font-size:5px;line-height:1.3}
.desc{position:absolute;top:198px;width:100px;font-size:5px;line-height:1.35;color:#555}
.section-label{position:absolute;top:108px;height:40px;background:var(--orange);color:#fff;font-size:19px;font-weight:700;font-style:italic;display:flex;align-items:center;justify-content:center;border-radius:3px}
.section-intro{position:absolute;top:170px;left:10px;width:228px;text-align:center;font-size:5.5px;font-style:italic;color:#555}
.folio{position:absolute;bottom:8px;font-size:5px;color:var(--muted)}
.page.left .folio{left:12px}
.page.right .folio{right:12px}
/* cover */
.season{position:absolute;top:8px;right:14px;font-size:5px;color:var(--muted)}
.url-band{position:absolute;left:0;top:172px;width:228px;height:50px;background:var(--orange);color:#fff;font-size:14px;font-weight:700;display:flex;align-items:center;padding-left:20px;border-radius:0 3px 3px 0}
.cover-title{position:absolute;left:20px;top:150px;width:200px;height:62px;background:var(--orange);color:#fff;text-align:center;padding-top:6px;border-radius:3px}
.cover-title small{display:block;font-size:6px;font-weight:600}
.cover-title strong{display:block;font-size:24px;font-weight:700;line-height:1.4}
.cover-url{position:absolute;top:226px;left:0;width:248px;text-align:center;font-size:5.5px;color:#555}
/* contact + contents */
.contact{position:absolute;left:48px;top:26px;font-size:5px;line-height:1.4;color:#444}
.contact .name{font-size:8px;font-weight:700;font-style:italic;margin-bottom:6px}
.contact .web{font-size:7px;font-weight:700;margin-top:16px;margin-left:-10px}
.contents{position:absolute;left:10px;top:24px;border-collapse:collapse;font-size:5.5px;color:#444}
.contents td{padding:1.5px 8px 1.5px 0}
</style>
</head>
<body>

<!-- Spread 1: cover -->
<section class="spread" style="left:82px;top:22px">
  <div class="page left">
    <div class="ghost">sorel bunt</div>
    <div class="url-band">www.sorel-bunt.com</div>
  </div>
  <div class="page right">
    <div class="season">Sommer/Herbst 2009</div>
    <div class="running" style="top:26px;left:40px">Exklusiv in Deutschland bei sorel bunt</div>
    <div class="frame" style="top:40px;height:130px">
      <div class="photo" role="img" aria-label="Zwei doppelwandige Edelstahlschalen mit Obst" style="background:radial-gradient(ellipse at 55% 40%,#fafafa 0%,#cfd2d4 40%,#8e9396 70%,#f4f4f4 100%)"></div>
    </div>
    <div class="cover-title"><small>Wohn- und Tischkultur, Lifestyle, Gartendeko</small><strong>Sorel bunt</strong></div>
    <div class="cover-url">www.sorel-bunt.com</div>
  </div>
</section>

<!-- Spread 2: contact + contents -->
<section class="spread" style="left:620px;top:22px">
  <div class="page left">
    <div class="ghost">sorel bunt</div>
    <div class="running">Exklusiv in Deutschland bei sorel bunt</div>
    <div class="frame">
      <div class="contact">
        <div class="name">sorel bunt</div>
        Inh. Lena Sorel<br>Lindenweg 7<br>50667 Köln<br><br>info@sorel-bunt.com<br>Tel. 0221 4471 203
        <div class="web">www.sorel-bunt.com</div>
      </div>
    </div>
    <div class="folio">3</div>
  </div>
  <div class="page right">
    <div class="ghost">sorel bunt</div>
    <div class="running">Wohn- und Tischkultur, Lifestyle, Gartendeko</div>
    <div class="frame">
      <table class="contents">
        <tr><td>01 Schalen</td><td>Seite</td><td>5-12</td></tr>
        <tr><td>02 Teelichthalter</td><td>Seite</td><td>13-18</td></tr>
        <tr><td>03 Fröhliche Tierwelt</td><td>Seite</td><td>19-24</td></tr>
        <tr><td>04 Bänder und Haken</td><td>Seite</td><td>25</td></tr>
        <tr><td>05 Rosenbuschwerk</td><td>Seite</td><td></td></tr>
      </table>
    </div>
    <div class="tab">Inhalt</div>
    <div class="folio">4</div>
  </div>
</section>

<!-- Spread 3: Schalen intro -->
<section class="spread" style="left:82px;top:297px">
  <div class="page left">
    <div class="ghost">sorel bunt</div>
    <div class="running">Exklusiv in Deutschland bei sorel bunt</div>
    <div class="frame"></div>
    <div class="section-label" style="left:10px;width:212px">01 Schalen</div>
    <div class="section-intro">Eine wunderschöne Kollektion lebensmittelechter Schalen</div>
    <div class="folio">5</div>
  </div>
  <div class="page right">
    <div class="ghost">sorel bunt</div>
    <div class="running">Wohn- und Tischkultur, Lifestyle, Gartendeko</div>
    <div class="frame">
      <div class="photo" role="img" aria-label="Bauchige Edelstahlschale mit Obst" style="background:radial-gradient(ellipse at 50% 45%,#f7f7f7 0%,#c9ccce 45%,#8c9194 70%,#fff 100%)"></div>
    </div>
    <div class="tab">Schalen</div>
    <div class="caption" style="left:12px"><strong>Bauchige Schale</strong><span>doppelwandig<br>30 cm</span></div>
    <div class="desc" style="left:118px">Die Schale aus gebürstetem Edelstahl hält Obst länger frisch und kühl.</div>
    <div class="folio">6</div>
  </div>
</section>

<!-- Spread 4: Schalen products -->
<section class="spread" style="left:620px;top:297px">
  <div class="page left">
    <div class="ghost">sorel bunt</div>
    <div class="running">Exklusiv in Deutschland bei sorel bunt</div>
    <div class="frame">
      <div class="photo" role="img" aria-label="Doppelwandige Edelstahlschalen in vier Größen mit Himbeeren" style="background:radial-gradient(ellipse at 50% 55%,#f2f2f2 0%,#b9bdc0 45%,#7c8184 68%,#fff 100%)"></div>
    </div>
    <div class="tab">Schalen</div>
    <div class="desc" style="left:14px">Die Edelstahlschalen sind in vier Größen als Set oder einzeln erhältlich.</div>
    <div class="caption" style="left:130px;width:108px"><strong>Doppelwandschale</strong><span>doppelwandig<br>15, 20, 25 und 30 cm</span></div>
    <div class="folio">7</div>
  </div>
  <div class="page right">
    <div class="ghost">sorel bunt</div>
    <div class="running">Wohn- und Tischkultur, Lifestyle, Gartendeko</div>
    <div class="frame">
      <div class="photo" role="img" aria-label="Flache Edelstahlschale in freier Form" style="background:radial-gradient(ellipse at 50% 50%,#d7dadc 0%,#9aa0a3 45%,#5f6568 62%,#fff 76%)"></div>
    </div>
    <div class="tab">Schalen</div>
    <div class="caption" style="left:12px"><strong>Folienschale</strong><span>30 und 45 cm</span></div>
    <div class="desc" style="left:118px">Jede Schale ein Unikat, von Hand geformt.</div>
    <div class="folio">8</div>
  </div>
</section>

<!-- Spread 5: Teelichthalter -->
<section class="spread" style="left:82px;top:572px">
  <div class="page left">
    <div class="ghost">sorel bunt</div>
    <div class="running">Exklusiv in Deutschland bei sorel bunt</div>
    <div class="frame">
      <div class="photo" role="img" aria-label="Teelichthalter aus Glas auf dunklem Sockel" style="background:radial-gradient(ellipse at 50% 50%,#eef0f0 0%,#c8ccce 40%,#5a5c5e 62%,#fff 78%)"></div>
    </div>
    <div class="tab long">Teelichthalter</div>
    <div class="desc" style="left:14px">Klares Glas auf massivem Sockel, ideal für Tisch und Fensterbank im Haus.</div>
    <div class="caption" style="left:130px"><strong>Brunnen</strong><span>klar, mundgeblasen<br>Höhe 14 cm</span></div>
    <div class="folio">13</div>
  </div>
  <div class="page right">
    <div class="ghost">sorel bunt</div>
    <div class="running">Wohn- und Tischkultur, Lifestyle, Gartendeko</div>
    <div class="frame">
      <div class="photo" role="img" aria-label="Hängende Teelichter aus farbigem Glas in Tropfenform" style="background:linear-gradient(90deg,#fff 0%,#f06a1f 22%,#fff 38%,#2aa6b5 50%,#fff 60%,#9cc43a 72%,#fff 82%,#d8307a 92%,#fff 100%)"></div>
    </div>
    <div class="tab long">Teelichthalter</div>
    <div class="caption" style="left:12px"><strong>Webernest</strong><span>orange, türkis, grün, pink<br>Glas</span></div>
    <div class="desc" style="left:118px">Mundgeblasene Glastropfen zum Aufhängen, für Garten und Wintergarten.</div>
    <div class="folio">14</div>
  </div>
</section>

<!-- Spread 6: Fröhliche Tierwelt -->
<section class="spread" style="left:620px;top:572px">
  <div class="page left">
    <div class="ghost">sorel bunt</div>
    <div class="running">Exklusiv in Deutschland bei sorel bunt</div>
    <div class="frame"></div>
    <div class="section-label" style="left:0;width:222px;font-size:16px">03 Föhliche Tierwelt</div>
    <div class="folio">19</div>
  </div>
  <div class="page right">
    <div class="ghost">sorel bunt</div>
    <div class="running">Wohn- und Tischkultur, Lifestyle, Gartendeko</div>
    <div class="frame">
      <div class="photo" role="img" aria-label="Vogelfiguren aus rostigem Metall auf Stäben" style="background:linear-gradient(180deg,#fff 0%,#e3d8cd 40%,#a37c5b 62%,#f4eee8 100%)"></div>
    </div>
    <div class="tab long">Fröhliche Tierwelt</div>
    <div class="caption" style="left:12px"><strong>Vögel am Stiel</strong><span>Metall, Rostoptik<br>div. Größen</span></div>
    <div class="desc" style="left:118px">Wetterfeste Gartenstecker aus Metall, jedes Stück von Hand gefertigt.</div>
    <div class="folio">20</div>
  </div>
</section>

</body>
</html>
```